Upper Fernbrook Historic District Banner

Our Historic district is located in Allentown Pennsylvania, USA and is in need of a new banner design. The banners measure 18" wide by 36" tall. The banners are hung upon decorative street lights approximately 7' above ground. The district is adjacent to a downtown area that is experiencing significant growth and economic revitalization. The district is in need of a banner that respects the historic nature of the neighborhood while also saying that this is a hip urban residential neighborhood. You can visit our website at www.upperfernbrook.org to learn more about our district. I also will upload our current logo which we like but think it may need some freshening up. I will also upload an image of one of the light poles.

just added a sketch of one thought that came up during one of my board meetings. We like the idea of keeping it simple, bold, easy to digest. we just upgraded many of our street signs in a black and white theme. thought it could be used in a playful positive and negative fashion. we also have previously liked color combinations of gold and blue - gold and black - gold and sepia - parchment and sepia

```html
<!DOCTYPE html>
<html lang="en">
<head>
<meta charset="utf-8">
<title>Upper Fernbrook Historic District Banner</title>
<link rel="stylesheet" href="https://fonts.googleapis.com/css2?family=Cinzel:wght@400&display=swap">
<style>
  :root {
    --parchment-light: #ddcc9f;
    --parchment-mid: #cfbb86;
    --parchment-dark: #b9a06a;
    --banner-red: #e8262a;
    --art-tint-a: #e6a98a;
    --art-tint-b: #d9735e;
  }
  html, body {
    margin: 0;
    padding: 0;
    width: 1200px;
    height: 2414px;
    overflow: hidden;
  }
  .banner {
    position: relative;
    width: 1200px;
    height: 2414px;
    overflow: hidden;
    background:
      radial-gradient(ellipse 700px 500px at 30% 20%, rgba(240, 226, 186, 0.55), transparent 70%),
      radial-gradient(ellipse 600px 800px at 75% 70%, rgba(236, 222, 180, 0.45), transparent 70%),
      radial-gradient(ellipse 900px 700px at 90% 95%, rgba(160, 128, 70, 0.35), transparent 70%),
      radial-gradient(ellipse 500px 600px at 5% 60%, rgba(175, 145, 90, 0.3), transparent 70%),
      linear-gradient(160deg, var(--parchment-light), var(--parchment-mid) 55%, var(--parchment-dark));
  }
  .banner-art {
    position: absolute;
    inset: 0;
    width: 1200px;
    height: 2414px;
  }
  .wordmark {
    font-family: "Cinzel", serif;
    font-weight: 400;
    fill: var(--banner-red);
  }
  .wordmark-initial { font-size: 300px; }
  .wordmark-line-one { font-size: 200px; }
  .wordmark-line-two { font-size: 205px; }
  .district-label { font-size: 92px; }
  .accent-rule {
    stroke: var(--banner-red);
    stroke-width: 6;
    stroke-linecap: round;
  }
</style>
</head>
<body>
  <main class="banner">
    <svg class="banner-art" viewBox="0 0 1200 2414" xmlns="http://www.w3.org/2000/svg">
      <defs>
        <linearGradient id="building-tint" x1="0" y1="0" x2="1" y2="1">
          <stop offset="0" stop-color="var(--art-tint-a)"/>
          <stop offset="1" stop-color="var(--art-tint-b)"/>
        </linearGradient>
      </defs>
      <g transform="translate(600 1207) rotate(-63)">
        <rect class="building-illustration" x="240" y="-800" width="640" height="720"
              fill="url(#building-tint)" opacity="0.75"
              role="img" aria-label="Line drawing of a historic house tower with a pointed roof and arched window"/>

        <text class="wordmark wordmark-line-one" x="-560" y="0"><tspan class="wordmark-initial">U</tspan>PPER</text>
        <text class="wordmark wordmark-line-two" x="-930" y="200" textLength="1815" lengthAdjust="spacingAndGlyphs">FERNBROOK</text>

        <line class="accent-rule" x1="-620" y1="315" x2="720" y2="290"/>

        <text class="wordmark district-label" x="-1050" y="440">Historic District</text>
      </g>
    </svg>
  </main>
</body>
</html>
```